Business Card Design for Event Planning Company

Create a business card for event planning company using our new logo. After I pick the design, I will need files made for 6 employees. Our company provides event design & logistics services as well as venue management. The font should be sans serif and complementary to the logo. I will need to know the name of the font selected for the final design. The phone numbers listed should be separated by "." not "-"

Address for the card
PO Box 318, Washington, DC 20019

Card One
Lorna Pettibone
lpettibone@galavoyant.com
202.481.7730

Card Two
Miriam Okonkwo
mokonkwo@galavoyant.com
202.556.2047

Card Three
Tessa Varnholt
tvarnholt@galavoyant.com
978.620.4471

Card Four
Robin Fess
rfess@galavoyant.com
202.718.3362

Card Five
Ada-Rose Pelletan-Uzor
adarose@galavoyant.com
202.839.1205

Card Six
Beatrix Holloway
Beatrix@galavoyant.com
202.492.6618

Target Market(s)

Corporate/Non-Profit

Industry/Entity Type

Event Planning

Contact Information for Business Card

Address for the card

Card One
Lorna Pettibone
lpettibone@galavoyant.com
202.481.7730

Card Two
Miriam Okonkwo
202.556.2047

Card Three
Tessa Varnholt
978.620.4471

Card Four
Robin Fess
rfess@galavoyant.com
202.718.3362

Card Five
Ada-Rose Pelletan-Uzor
202.839.1205

Card Six
Beatrix Holloway
202.492.6618

Font styles to use
Sans Serif

Colors

Designer to choose colors to be used in the design.

Requirements
Must have
• Two-sided with logo
Should not have
• Extra colors or be too busy

```html
<!DOCTYPE html>
<html lang="en">
<head>
<meta charset="utf-8">
<title>Galavoyant Business Card</title>
<link rel="stylesheet" href="https://fonts.googleapis.com/css2?family=Questrial&family=Montserrat:wght@600&display=swap">
<style>
  :root {
    --teal: #5fa3a2;
    --ink: #000000;
    --paper: #ffffff;
    --backdrop: #e9e7e3;
  }
  * { margin: 0; padding: 0; box-sizing: border-box; }
  html, body { width: 1200px; height: 1155px; overflow: hidden; background: var(--backdrop); }
  .canvas { position: relative; width: 1200px; height: 1155px; }
  .card {
    position: absolute;
    width: 894px; height: 512px;
    border-radius: 22px;
    overflow: hidden;
    background: var(--ink);
    box-shadow: 0 2px 10px rgba(0,0,0,0.25);
  }
  .card-front { left: 45px; top: 51px; }
  .card-back { left: 248px; top: 605px; }
  .card-decor {
    position: absolute;
    inset: 0;
    background:
      linear-gradient(to bottom, rgba(95,163,162,0) 55%, var(--teal) 78%),
      radial-gradient(ellipse 420px 360px at 28% 15%, var(--paper) 0%, var(--paper) 55%, var(--ink) 100%);
  }
  .brand-name {
    position: absolute;
    font-family: "Questrial", sans-serif;
    line-height: 1;
    white-space: nowrap;
  }
  .card-front .brand-name {
    left: 0; width: 534px; top: 148px;
    text-align: center;
    font-size: 66px;
    color: var(--teal);
    letter-spacing: -0.5px;
  }
  .brand-dot {
    position: absolute;
    left: 243px; top: 66px;
    width: 48px; height: 48px;
    border-radius: 50%;
    background: var(--teal);
  }
  .person-name {
    position: absolute;
    right: 38px; top: 58px;
    font-family: "Montserrat", sans-serif;
    font-weight: 600;
    font-size: 33px;
    color: var(--paper);
    letter-spacing: 0.5px;
  }
  .address, .contact {
    position: absolute;
    font-family: "Questrial", sans-serif;
    font-style: normal;
    font-size: 21px;
    color: var(--paper);
    line-height: 36px;
  }
  .address { left: 38px; top: 418px; }
  .contact { right: 24px; top: 414px; text-align: right; }
  .contact-line { display: flex; justify-content: flex-end; align-items: center; gap: 10px; }
  .contact-icon { width: 22px; height: 22px; flex: none; }
  .card-back .brand-name {
    left: 0; right: 0; top: 170px;
    text-align: center;
    font-size: 104px;
    color: var(--paper);
  }
  .website {
    position: absolute;
    left: 0; right: 0; top: 370px;
    text-align: center;
    font-family: "Questrial", sans-serif;
    font-size: 27px;
    letter-spacing: 6px;
    color: var(--paper);
  }
</style>
</head>
<body>
<main class="canvas">

  <section class="card card-front" aria-label="Card front">
    <div class="card-decor" role="img" aria-label="Decorative background: white oval at top left over black, with a teal wave band along the bottom"></div>
    <span class="brand-dot" aria-hidden="true"></span>
    <p class="brand-name">galavoyant</p>
    <h1 class="person-name">Lorna Pettibone</h1>
    <address class="address">
      <span>PO Box 318</span><br>
      <span>Washington, DC 20019</span>
    </address>
    <div class="contact">
      <p class="contact-line">
        <svg class="contact-icon" viewBox="0 0 22 22" aria-hidden="true">
          <rect x="6" y="2" width="10" height="18" rx="2" fill="none" stroke="var(--paper)" stroke-width="2"/>
          <rect x="8" y="5" width="6" height="5" fill="var(--paper)"/>
          <rect x="8" y="12" width="6" height="5" fill="var(--paper)" opacity="0.8"/>
        </svg>
        <span>202.481.7730</span>
      </p>
      <p class="contact-line">
        <svg class="contact-icon" viewBox="0 0 22 22" aria-hidden="true">
          <path d="M2,9 L11,3 L20,9 L20,19 L2,19 Z" fill="var(--paper)"/>
          <path d="M2,9 L11,15 L20,9" fill="none" stroke="var(--teal)" stroke-width="1.6"/>
        </svg>
        <span>lpettibone@galavoyant.com</span>
      </p>
    </div>
  </section>

  <section class="card card-back" aria-label="Card back">
    <p class="brand-name">galavoyant</p>
    <p class="website">www.galavoyant.com</p>
  </section>

</main>
</body>
</html>
```